New business card for Building services company

I own a small 1 person business which primarily works at heights. I gain access to my work areas via ladders and use safety harnesses. I conduct gutter cleaning, roof cleaning with a pressure cleaner(water blaster), ground level pressure cleaning (driveways, footpaths and walls), I also do small handy-man jobs & gardening/ tree trimming.

I have just had a logo designed by Sketch Hive, which I will upload. I'd like to see the themes followed through.
I like the colour of aqua or the colours what is in the logo.

I live in tropical north Queensland in Cairns, Australia. It is where the rain forest meets the Coral Lantern Shoal. On average it is 30+ degrees C.
Updates

Hello all designers. Thankyou for all the submissions so far. The following are my business details which I need on the card-

VERNO Roof, Gutter & Pressure Cleaning Services.
Director -Dale Marwick
Ph 0417385026
Email- roofcleaning@plovernet.example.au
ABN -48 902 317 254

Please include the following services which my business conducts-
*Gutter Cleaning
*Pressure Cleaning- Roof's, Driveways etc
*Minor Roof, Gutter & Building Maintenance
*Garden waste removal & complex cleanups

Public Liability upto $10 Million
Working at Heights Cert.

Quote-                                     Date-

Hi everyone,  could you please ensure you have -"Quote" and "Date" on the card. I'll need space to hand write details on the card for the specific details.        

Requirements
Must have
• The logo attached must be included.
• The rear side of the card is dedicated to job quoted and price of the job.
• *Please include- Quote price, Quote date. etc
• Including the tasks I do at work around the side of the card- Gutter Cleaning; Roof Cleaning, Gutter Maintenance; Gardening; Pressure Cleaning Roof's, Driveways etc.
Nice to have
• The rear side to have a ladder

```html
<!DOCTYPE html>
<html lang="en">
<head>
<meta charset="utf-8">
<title>VERNO Business Card</title>
<link rel="stylesheet" href="https://fonts.googleapis.com/css2?family=Bebas+Neue&family=Open+Sans:wght@300;400;600;700&family=Roboto+Condensed:wght@300;400&display=swap">
<style>
  :root {
    --page: #e9eef2;
    --card: #d5eef9;
    --cyan: #29c4ee;
    --cyan-deep: #1a7fd0;
    --navy: #2e3192;
    --ink: #1d2a3a;
    --link: #2a9fd6;
    --call: #5b6f86;
    --white: #ffffff;
  }
  * { margin: 0; padding: 0; box-sizing: border-box; }
  html, body { width: 1200px; height: 900px; overflow: hidden; }
  body { position: relative; background: var(--page); font-family: "Open Sans", sans-serif; }

  .card { position: absolute; background: var(--card); box-shadow: 0 6px 14px rgba(0,0,0,.35); }
  .card-front { left: 312px; top: 62px; width: 575px; height: 319px; }
  .card-back { left: 312px; top: 487px; width: 579px; height: 320px; }

  .abs { position: absolute; }

  /* front */
  .side-strip { left: 0; top: 0; width: 37px; height: 319px; background: var(--cyan); }
  .side-rule { left: 0; width: 37px; height: 3px; background: var(--card); }
  .side-rule.one { top: 176px; }
  .side-rule.two { top: 216px; }

  .brand-name { left: 118px; top: 32px; width: 264px; text-align: center; font-weight: 600; font-size: 62px; line-height: 1; color: var(--navy); letter-spacing: 1px; }
  .brand-mark { left: 398px; top: 20px; width: 80px; height: 80px; background: var(--navy); }
  .brand-tagline { left: 118px; top: 105px; width: 264px; text-align: center; font-size: 7.5px; font-weight: 700; color: var(--navy); white-space: nowrap; }
  .brand-call { left: 118px; top: 117px; width: 264px; text-align: center; font-size: 13px; font-weight: 600; color: var(--call); letter-spacing: .5px; }

  .services { display: flex; align-items: center; justify-content: center; gap: 5px; border-radius: 14px; font-family: "Roboto Condensed", sans-serif; font-weight: 300; font-size: 10.5px; letter-spacing: -0.2px; color: var(--white); white-space: nowrap; overflow: hidden; }
  .services-front { left: 45px; top: 147px; width: 492px; height: 28px; background: var(--cyan); }

  .holder-name { left: 55px; top: 198px; font-family: "Bebas Neue", sans-serif; font-size: 28px; color: var(--navy); letter-spacing: .5px; }
  .holder-role { left: 153px; top: 228px; font-size: 10px; font-weight: 600; color: var(--navy); }

  .contact { left: 328px; font-size: 11px; color: var(--link); display: flex; align-items: center; gap: 20px; white-space: nowrap; }
  .contact svg { width: 13px; height: 13px; }
  .contact.phone { top: 194px; }
  .contact.mail { top: 213px; }
  .contact.abn { top: 230px; left: 367px; font-size: 12.5px; letter-spacing: .4px; }

  .cover-band { left: 37px; top: 263px; width: 538px; height: 43px; background: var(--cyan); }
  .cover-text { left: 37px; top: 267px; width: 538px; text-align: center; font-size: 12px; line-height: 14px; color: var(--white); }
  .fill-field { top: 283px; font-size: 10px; color: var(--white); }
  .fill-field .line { display: inline-block; width: 76px; border-bottom: 1px solid var(--white); margin-left: 2px; }
  .fill-field.quote { left: 45px; }
  .fill-field.date { left: 427px; }

  /* back */
  .back-panel { left: 38px; top: 34px; width: 503px; height: 250px; background: var(--cyan); }
  .back-name { left: 0; top: 30px; width: 503px; text-align: center; font-weight: 300; font-size: 34px; line-height: 40px; color: var(--white); letter-spacing: 1px; }
  .back-line { left: 0; width: 503px; text-align: center; font-size: 14px; color: var(--ink); white-space: nowrap; }
  .back-line.l1 { top: 81px; }
  .back-line.l2 { top: 111px; }
  .back-line.l3 { top: 142px; }
  .back-line.l4 { top: 172px; }
  .back-line .label { color: var(--white); }
  .services-back { left: 5px; top: 222px; width: 491px; height: 26px; background: var(--cyan-deep); }
</style>
</head>
<body>

<section class="card card-front" aria-label="Card front">
  <div class="abs side-strip"></div>
  <div class="abs side-rule one"></div>
  <div class="abs side-rule two"></div>

  <div class="abs brand-name">VERNO</div>
  <div class="abs brand-mark"></div>
  <div class="abs brand-tagline">ROOF, GUTTER &amp; PRESSURE CLEANING SERVICES</div>
  <div class="abs brand-call">CALL 0417 385 026</div>

  <div class="abs services services-front">
    <span>Gutter Cleaning</span><span>|</span>
    <span>Roof Cleaning</span><span>|</span>
    <span>Gutter Maintenance</span><span>|</span>
    <span>Gardening</span><span>|</span>
    <span>Pressure Cleaning Roof's</span><span>|</span>
    <span>Driveways</span>
  </div>

  <div class="abs holder-name">DALE MARWICK</div>
  <div class="abs holder-role">Director</div>

  <div class="abs contact phone">
    <svg viewBox="0 0 16 16" aria-hidden="true"><path d="M4 1h3l1 4-2 1.5c1 2 2.5 3.5 4.5 4.5L12 9l4 1v3c0 1-1 2-2 2C7 15 1 9 1 3c0-1 1-2 3-2z" fill="var(--link)"/></svg>
    <span>0417 385 026</span>
  </div>
  <div class="abs contact mail">
    <svg viewBox="0 0 16 16" aria-hidden="true"><rect x="1" y="3" width="14" height="10" fill="none" stroke="var(--link)" stroke-width="1.3"/><path d="M1 3l7 6 7-6" fill="none" stroke="var(--link)" stroke-width="1.3"/></svg>
    <span>roofcleaning@plovernet.example.au</span>
  </div>
  <div class="abs contact abn">ABN -48 902 317 254</div>

  <div class="abs cover-band"></div>
  <div class="abs cover-text">Public Liability upto $10 Million<br>Working at Heights Cert.</div>
  <div class="abs fill-field quote">Quote:<span class="line"></span></div>
  <div class="abs fill-field date">Date:<span class="line"></span></div>
</section>

<section class="card card-back" aria-label="Card back">
  <div class="abs back-panel">
    <div class="abs back-name">VERNO</div>
    <div class="abs back-line l1">ROOF, GUTTER &amp; PRESSURE</div>
    <div class="abs back-line l2">CELANING SERVICES</div>
    <div class="abs back-line l3"><span class="label">CALL :</span>&nbsp; 0417 385 026</div>
    <div class="abs back-line l4"><span class="label">E-mail:</span> roofcleaning@plovernet.example.au</div>
    <div class="abs services services-back">
      <span>Gutter Cleaning</span><span>|</span>
      <span>Roof Cleaning</span><span>|</span>
      <span>Gutter Maintenance</span><span>|</span>
      <span>Gardening</span><span>|</span>
      <span>Pressure Cleaning Roof's</span><span>|</span>
      <span>Driveways</span>
    </div>
  </div>
</section>

</body>
</html>
```